KB Rubbish Removal Business Card

Hey,
I need a double sided business card designed for a rubbish removal business based in Australia. Logo is already chosen, similar colours preferred for both sides of the business card.

Details to include:

Front:

KB Rubbish Removal
Darren Holloway
Managing Director
Mobile: 0471 902 146
Email: darren@kbrubbishremoval.com.au
Website: kbrubbishremoval.com.au

Rear:

How did we do?
kbrubbishremoval.com.au/review

```html
<!DOCTYPE html>
<html lang="en">
<head>
<meta charset="utf-8">
<title>KB Rubbish Removal – Business Card</title>
<link href="https://fonts.googleapis.com/css2?family=Poppins:wght@600&family=Questrial&display=swap" rel="stylesheet">
<style>
  :root {
    --backdrop: #2a2a2a;
    --card: #ffffff;
    --green-light: #6cc24a;
    --green-bright: #3cb54a;
    --green-mid: #22963f;
    --green-deep: #157a3a;
    --ink: #555555;
    --ink-dark: #4a4a4a;
  }
  * { box-sizing: border-box; margin: 0; padding: 0; }
  html, body { width: 1200px; height: 900px; overflow: hidden; }
  body { background: var(--backdrop); position: relative; font-family: "Questrial", sans-serif; }

  .card {
    position: absolute;
    top: 308px;
    width: 473px;
    height: 285px;
    background: var(--card);
    box-shadow: 0 6px 16px rgba(0,0,0,0.55);
    overflow: hidden;
  }
  .card--front { left: 97px; }
  .card--back { left: 630px; }

  .accent-band {
    position: absolute;
    background: linear-gradient(90deg, var(--green-bright), var(--green-deep) 55%, var(--green-mid));
  }
  .accent-band--front { left: 0; top: 0; width: 315px; height: 26px; }
  .accent-band--back { left: 159px; bottom: 0; width: 314px; height: 68px; }

  .brand {
    position: absolute;
    left: 0;
    width: 244px;
    top: 40px;
    text-align: center;
  }
  .brand__dot {
    display: block;
    width: 96px;
    height: 96px;
    margin: 0 auto;
    border-radius: 50%;
    background: var(--green-mid);
  }
  .brand__name {
    display: block;
    margin-top: 16px;
    font-family: "Poppins", sans-serif;
    font-weight: 600;
    font-size: 12.8px;
    color: var(--ink-dark);
  }

  .person { position: absolute; left: 218px; top: 126px; }
  .person__name {
    font-family: "Poppins", sans-serif;
    font-weight: 600;
    font-size: 20px;
    line-height: 1;
    color: var(--green-light);
    letter-spacing: -0.3px;
  }
  .person__role {
    margin-top: 4px;
    font-size: 12.5px;
    color: var(--ink);
  }

  .contacts { position: absolute; left: 218px; top: 183px; list-style: none; }
  .contacts__item {
    display: flex;
    align-items: center;
    height: 17px;
    margin-bottom: 12.5px;
    font-size: 13.5px;
    color: var(--ink);
  }
  .contacts__icon {
    width: 16px;
    height: 16px;
    margin-right: 4px;
    flex: none;
  }

  .review { position: absolute; right: 37px; top: 174px; text-align: right; }
  .review__title {
    font-family: "Poppins", sans-serif;
    font-weight: 600;
    font-size: 19px;
    line-height: 1;
    color: var(--green-light);
    margin-right: 3px;
  }
  .review__url {
    margin-top: 4px;
    font-size: 11.5px;
    color: var(--ink-dark);
  }
</style>
</head>
<body>

<section class="card card--front" aria-label="Business card front">
  <div class="accent-band accent-band--front" role="img" aria-label="Green decorative wave artwork"></div>

  <div class="brand">
    <span class="brand__dot"></span>
    <span class="brand__name">KB RUBBISH REMOVAL</span>
  </div>

  <div class="person">
    <h1 class="person__name">DARREN HOLLOWAY</h1>
    <p class="person__role">MANAGING DIRECTOR</p>
  </div>

  <ul class="contacts">
    <li class="contacts__item">
      <svg class="contacts__icon" viewBox="0 0 16 16" aria-hidden="true">
        <circle cx="8" cy="8" r="8" fill="var(--green-bright)"/>
        <path d="M5.2,4 L6.6,4 L7.2,5.9 L6.3,6.6 C6.8,7.8 7.9,8.9 9.2,9.5 L9.9,8.6 L11.8,9.2 L11.8,10.6 C11.8,11.2 11.3,11.7 10.7,11.6 C7.3,11.2 4.6,8.5 4.2,5.1 C4.1,4.5 4.6,4 5.2,4 Z" fill="#fff"/>
      </svg>
      0471 902 146
    </li>
    <li class="contacts__item">
      <svg class="contacts__icon" viewBox="0 0 16 16" aria-hidden="true">
        <circle cx="8" cy="8" r="8" fill="var(--green-bright)"/>
        <rect x="4" y="5" width="8" height="6" rx="0.6" fill="#fff"/>
        <path d="M4.3,5.4 L8,8.4 L11.7,5.4 M4.3,10.6 L6.8,7.8 M11.7,10.6 L9.2,7.8" stroke="var(--green-bright)" stroke-width="0.8" fill="none"/>
      </svg>
      darren@kbrubbishremoval.com.au
    </li>
    <li class="contacts__item">
      <svg class="contacts__icon" viewBox="0 0 16 16" aria-hidden="true">
        <circle cx="8" cy="8" r="8" fill="var(--green-bright)"/>
        <g stroke="#fff" stroke-width="0.8" fill="none">
          <circle cx="8" cy="8" r="4.2"/>
          <ellipse cx="8" cy="8" rx="1.8" ry="4.2"/>
          <path d="M3.8,8 H12.2 M4.4,6 H11.6 M4.4,10 H11.6"/>
        </g>
      </svg>
      kbrubbishremoval.com.au
    </li>
  </ul>
</section>

<section class="card card--back" aria-label="Business card back">
  <div class="accent-band accent-band--back" role="img" aria-label="Green decorative wave artwork"></div>

  <div class="review">
    <h2 class="review__title">HOW DID WE DO?</h2>
    <p class="review__url">kbrubbishremoval.com.au/review</p>
  </div>
</section>

</body>
</html>
```